Company Business Card Design Project - Revamp the image of an old construction company.

We need a business card designed for a new company in Australia.

Type of business is Commercial Roofing & Painting.

Medium will be brushed black metal card that can/will be acid etched to a brushed steel silver, acid die cut and two printed colours of our choice which will be white and pantone orange.

We have hopes that the design will be simple, modern and represent with a quick glance what our company does.

Please read instructions carefully in must have box any questions please ask.

If you are interested in this job please look at other job that we have which is very similar with logo and design

Please have a look at the things that can be done with metals cards on google images for inspiration.

Target Market(s)

Business owners, commercial property development Men from 25-70 years of age.

Industry/Entity Type

Construction

Requirements
Must have
• Front of card:

Must use the company logo and name provided as attachment (see below norwick vale construction_black_background).

the words -Commercial Painting and Roofing- must be on front of card

details needed on front or back depending on your design

Name
position
email
mobile

all details can be on front with a cool design to be etched on the back of card or to keep front simple you can put all detail on back of card, I will leave the lay out to you.

Colours in logo are

Pantone 144 C Orange
Pantone 11-0601 White
Pantone 7539 C Gray
Pantone 426 C Black

However black will be the base of black metal card. Gray will be replaced with the etching in card revealing the silver. Orange and white will be printed on card.

Please have fun!!
Should not have
• Please don't clutter the card
No fonts smaller then 7 points

```html
<!DOCTYPE html>
<html lang="en">
<head>
<meta charset="utf-8">
<title>Norwick Vale – Business Card</title>
<link rel="stylesheet" href="https://fonts.googleapis.com/css2?family=Open+Sans:wght@400;600&display=swap">
<style>
  :root {
    --card-black: #0d0c19;
    --etch-silver: #9a9d9a;
    --etch-dark: #3a3a44;
    --print-white: #ffffff;
    --print-orange: #f39322;
    --gap-white: #ffffff;
  }
  html, body {
    margin: 0;
    padding: 0;
    overflow: hidden;
    background: var(--gap-white);
  }
  .canvas {
    position: relative;
    width: 1200px;
    height: 353px;
    background: var(--gap-white);
    font-family: "Open Sans", Arial, sans-serif;
    color: var(--print-white);
  }
  .card {
    position: absolute;
    top: 0;
    height: 353px;
    background: var(--card-black);
    overflow: hidden;
  }
  .card--front { left: 0; width: 597px; }
  .card--back { left: 603px; width: 597px; }

  .etch-band {
    position: absolute;
    left: 0;
    width: 100%;
    background: linear-gradient(180deg, var(--etch-dark), var(--etch-silver) 45%, var(--etch-dark));
    opacity: 0.75;
  }
  .etch-band--top { top: 0; height: 58px; }
  .etch-band--bottom { top: 287px; height: 66px; }

  .brand {
    position: absolute;
    left: 106px;
    top: 122px;
    display: flex;
    align-items: center;
    gap: 16px;
  }
  .brand__mark {
    width: 64px;
    height: 64px;
    background: var(--etch-silver);
  }
  .brand__name {
    font-weight: 600;
    font-size: 40px;
    letter-spacing: 1px;
    color: var(--etch-silver);
    white-space: nowrap;
  }

  .house-art {
    position: absolute;
    left: 425px;
    top: 206px;
    width: 156px;
    height: 124px;
    background: linear-gradient(180deg, var(--print-orange), rgba(243,147,34,0.55));
  }

  .tagline {
    position: absolute;
    left: 128px;
    top: 302px;
    padding: 4px 12px;
    background: var(--card-black);
    font-size: 19px;
    line-height: 28px;
    color: var(--print-white);
  }

  .divider {
    position: absolute;
    left: 296px;
    top: 48px;
    width: 2px;
    height: 252px;
    background: var(--etch-silver);
    opacity: 0.8;
  }
  .person {
    position: absolute;
    left: 40px;
    top: 150px;
    width: 226px;
    text-align: center;
    font-size: 16px;
    line-height: 24px;
  }
  .contact {
    position: absolute;
    left: 320px;
    top: 84px;
    width: 250px;
    text-align: center;
    font-size: 16px;
    line-height: 22px;
  }
  .contact p { margin: 0; }
  .contact__email, .contact__phone { margin-bottom: 22px !important; }
</style>
</head>
<body>
<div class="canvas">
  <section class="card card--front">
    <div class="etch-band etch-band--top" role="img" aria-label="Etched brushed-steel texture band"></div>
    <div class="etch-band etch-band--bottom" role="img" aria-label="Etched brushed-steel texture band"></div>
    <div class="brand">
      <span class="brand__mark"></span>
      <span class="brand__name">NORWICK VALE</span>
    </div>
    <div class="house-art" role="img" aria-label="Brush-painted orange roof outline illustration"></div>
    <p class="tagline">Commercial Painting and Roofing</p>
  </section>

  <section class="card card--back">
    <div class="person">
      <div class="person__name">Liam Carter</div>
      <div class="person__role">Director</div>
    </div>
    <div class="divider"></div>
    <div class="contact">
      <p class="contact__email">liamc@norwickvale.com</p>
      <p class="contact__phone">+ 61 0412 555 918</p>
      <p class="contact__address">41, harlow house,<br>Bay Street,<br>Sydney.2000<br>Australia</p>
    </div>
  </section>
</div>
</body>
</html>
```